Label for Sports Nutrition Supplement

I need a label design for a pre-workout sports nutrition supplement. A pre-workout supplement helps increase energy, strength, stamina, and endurance.

The name of the company is Tallcrest Nutrition

The demographic is males between the ages of 18-35 who like to workout to stay in shape.

I'd like to see designs that have a red (#FF0000), black, and white color. The container will be black and similar to this one:

https://www.shopvarlo.example/Dunmere-Vigor-Works-Workout-Supplement/item/Q4827KXPLM

Some designs that caught my attention are:

a) http://www.brivello-fizz.example/stories/brivello-zero-sugar-new-and-improved-sugar-free-brivello-launches-this-summer

b) The Brivo Zero can (2nd can from the left side) http://dailyhalden.example/2015/03/09/brivello-is-trialling-new-unified-packaging-and-its-totally-different-4817362/

c) https://www.shopvarlo.example/KRV-Clinically-Pulsevane-Testosterone-Enhancing/item/Z318WQRTNB

d) https://www.shopvarlo.example/OLDEN-SURGE-Pre-Workout-Non-Habit-Forming-All-Natural/item/M562HJDKEV

e) http://www.craftplume.example/design-gallery/bison-pre-workout-48213

f) https://www.wrapjournal.example/features/comment/history-of-the-world-in-52-packs-10-the-dunhaven-flip-top-box-29-09-2015

This label should do the following 5 things:

a. Stand out
b. Be simple
c. Pass the 5 year old test
d. Trigger emotional engagement
e. Create iconic assets

You can read more about what these 5 elements mean here... https://www.tradelumen.example/sites/onmarketing/2014/07/23/the-five-things-product-packaging-must-do/

The final design should communicate increased physical performance.

The instructions of the label are attached and include the elements that need to appear in each section of the label.

The company logo is attached.

The barcode is attached.

Thank you.

Target Market(s)

Industry/Entity Type

Supplement

Font styles to use
Serif
Sans Serif

Colors
ec1f27
ffffff
000000

Requirements
Must have
• This label should do the following 5 things:
• a. Stand out
• b. Be simple
• c. Pass the 5 year old test
• d. Trigger emotional engagement
• e. Create iconic assets
• You can read more about what these 5 elements mean here... https://www.tradelumen.example/sites/onmarketing/2014/07/23/the-five-things-product-packaging-must-do/
• The final design should communicate increased physical performance.
• Red color should be this color of red... #FF0000
• Using a blue color is NOT a must have, BUT if you decide to use a blue color, use this color of blue ... #0019A8
Nice to have
• OPTIONAL >> These effects caught my attention and are 100% OPTIONAL. Use them only if you feel it will make a better design.
• 1) A text that goes from small to large, such as the GRAVELOX text shown here... https://www.gravelox-cereal.example/
• 2) A text that is vertical, such as the VAMBR text shown here...
• https://www.vambr-fit.example

```html
<!DOCTYPE html>
<html lang="en">
<head>
<meta charset="utf-8">
<title>Ascend Pre-Workout Label – Tallcrest Nutrition</title>
<link rel="stylesheet" href="https://fonts.googleapis.com/css2?family=Oswald:wght@300;500;700&display=swap">
<style>
  :root {
    --red: #e8232a;
    --white: #ffffff;
    --black: #141414;
    --ink: #1c1c1c;
    --page: #efeae2;
  }
  * { margin: 0; padding: 0; box-sizing: border-box; }
  html, body { width: 1158px; height: 1200px; overflow: hidden; background: var(--page); }
  .label {
    position: relative;
    width: 1158px;
    height: 1200px;
    font-family: "Oswald", sans-serif;
    overflow: hidden;
  }
  .label-shapes { position: absolute; inset: 0; }

  .brand-seal {
    position: absolute;
    left: 414px; top: 20px;
    width: 330px; height: 330px;
    border-radius: 50%;
    background: var(--white);
    border: 18px solid var(--red);
    display: flex; align-items: center; justify-content: center;
  }
  .brand-name {
    font-weight: 700;
    font-size: 50px;
    line-height: 1.05;
    text-align: center;
    color: var(--red);
    letter-spacing: 3px;
    text-transform: uppercase;
  }

  .product-name {
    position: absolute;
    left: 0; width: 100%;
    top: 385px;
    text-align: center;
    font-weight: 700;
    font-size: 190px;
    line-height: 1;
    letter-spacing: 10px;
    color: var(--red);
  }
  .product-type {
    position: absolute;
    left: 0; width: 100%;
    top: 590px;
    text-align: center;
    font-weight: 300;
    font-size: 100px;
    line-height: 1;
    color: var(--red);
    transform: rotate(-3deg);
  }

  .benefits { list-style: none; }
  .benefit {
    position: absolute;
    display: flex; align-items: center; gap: 16px;
    font-size: 38px;
    color: var(--ink);
    letter-spacing: 2px;
    transform: rotate(-3deg);
    transform-origin: left center;
    white-space: nowrap;
  }
  .benefit strong { font-weight: 700; }
  .benefit span { font-weight: 300; }
  .benefit svg { width: 58px; height: 38px; flex: none; }
  .benefit-strength { left: 400px; top: 730px; }
  .benefit-stamina { left: 290px; top: 798px; }
  .benefit-endurance { left: 178px; top: 866px; }

  .supplement-tag, .servings {
    position: absolute;
    color: var(--white);
    font-weight: 700;
    letter-spacing: 4px;
    transform-origin: left center;
    white-space: nowrap;
    line-height: 1;
  }
  .supplement-tag { left: 460px; top: 955px; font-size: 32px; transform: rotate(-8deg); }
  .servings { left: 200px; top: 1025px; font-size: 44px; transform: rotate(-4deg); }

  .net-weight {
    position: absolute;
    left: 0; width: 100%;
    bottom: 24px;
    text-align: center;
    font-weight: 300;
    font-size: 30px;
    letter-spacing: 1px;
    color: var(--white);
  }

  .flavor-badge {
    position: absolute;
    left: 856px; top: 880px;
    width: 260px; height: 260px;
  }
</style>
</head>
<body>
<main class="label">
  <svg class="label-shapes" viewBox="0 0 1158 1200" aria-hidden="true">
    <rect width="1158" height="1200" fill="var(--red)"/>
    <path class="white-field" d="M0 226 Q580 190 1158 178 L1158 760 Q600 960 0 960 Z" fill="var(--white)"/>
    <path class="black-base" d="M0 1110 Q700 1080 1158 830 L1158 1200 L0 1200 Z" fill="var(--black)"/>
  </svg>

  <div class="brand-seal">
    <p class="brand-name">Tallcrest<br>Nutrition</p>
  </div>

  <h1 class="product-name">ASCEND</h1>
  <p class="product-type">PRE-WORKOUT</p>

  <ul class="benefits">
    <li class="benefit benefit-strength">
      <svg viewBox="0 0 62 40"><path d="M2 22 L20 36 L60 4 L20 28 Z" fill="var(--red)"/></svg>
      <strong>STRENGTH</strong><span>(PUMPS)</span>
    </li>
    <li class="benefit benefit-stamina">
      <svg viewBox="0 0 62 40"><path d="M2 22 L20 36 L60 4 L20 28 Z" fill="var(--red)"/></svg>
      <strong>STAMINA</strong><span>(PERFORMANCE)</span>
    </li>
    <li class="benefit benefit-endurance">
      <svg viewBox="0 0 62 40"><path d="M2 22 L20 36 L60 4 L20 28 Z" fill="var(--red)"/></svg>
      <strong>ENDURANCE</strong><span>(FOCUS)</span>
    </li>
  </ul>

  <p class="supplement-tag">DIETARY SUPPLEMENT</p>
  <p class="servings">20 SERVINGS</p>

  <svg class="flavor-badge" viewBox="0 0 260 260">
    <defs>
      <radialGradient id="fruit-tones" cx="50%" cy="45%" r="55%">
        <stop offset="0" stop-color="#f6a13a"/>
        <stop offset="0.55" stop-color="#e7433a"/>
        <stop offset="1" stop-color="#8fbf3c"/>
      </radialGradient>
      <path id="badge-arc" d="M40 140 A90 90 0 0 0 220 140"/>
    </defs>
    <circle cx="130" cy="130" r="120" fill="var(--black)" stroke="var(--red)" stroke-width="5"/>
    <circle cx="130" cy="110" r="58" fill="url(#fruit-tones)" role="img" aria-label="Fruit punch illustration: citrus, kiwi and berries splashing into a glass"/>
    <text font-family="Oswald, sans-serif" font-weight="500" font-size="30" letter-spacing="4" fill="var(--red)">
      <textPath href="#badge-arc" startOffset="50%" text-anchor="middle">FRUIT PUNCH</textPath>
    </text>
    <path d="M22 128 l5 10 11 1 -8 7 3 11 -11 -6 -11 6 3 -11 -8 -7 11 -1 Z" fill="var(--red)"/>
    <path d="M238 112 l5 10 11 1 -8 7 3 11 -11 -6 -11 6 3 -11 -8 -7 11 -1 Z" fill="var(--red)"/>
  </svg>

  <p class="net-weight">NET WEIGHT 444 GRMS (0.98 LB)</p>
</main>
</body>
</html>
```